Lose Up To 1 LB Of Fat Per Day

We need a double sided street sign for our weight loss clinic. We need the doctors picture to the right side of the sign and we need a challenge “Lose Up To 1 Pound Of Fat Per Day” included in the signage.
Our color scheme for the clinic are black, white, teal and silver.
The phone number should be at the bottom of the sign
555-206–3948

Target Market(s)

Weight Loss

Font styles to use
Sans Serif

```html
<!DOCTYPE html>
<html lang="en">
<head>
<meta charset="UTF-8">
<title>Lose Up To 1 Pound Of Fat Per Day – Street Sign</title>
<link rel="stylesheet" href="https://fonts.googleapis.com/css2?family=Lexend:wght@400;700;800&display=swap">
<style>
  :root {
    --teal: #037b78;
    --teal-glow: #5aa79c;
    --purple: #862c7e;
    --purple-shadow: #5e4e80;
    --mint: #c8e0c4;
    --white: #ffffff;
    --suit: #1f2330;
    --suit-light: #3a3f52;
  }
  html, body {
    margin: 0;
    padding: 0;
    width: 1200px;
    height: 900px;
    overflow: hidden;
  }
  .sign {
    position: relative;
    width: 1200px;
    height: 900px;
    overflow: hidden;
    background:
      radial-gradient(circle at 180px 330px, var(--teal-glow) 0%, rgba(3,123,120,0) 300px),
      var(--teal);
    font-family: "Lexend", sans-serif;
  }
  .doctor-photo {
    position: absolute;
    left: 0;
    top: 152px;
    width: 462px;
    height: 748px;
    background: linear-gradient(180deg, var(--suit-light) 0%, var(--suit) 100%);
    border-radius: 160px 160px 0 0;
  }
  .artwork {
    position: absolute;
    inset: 0;
  }
  .headline {
    fill: var(--white);
    font-family: "Lexend", sans-serif;
    font-weight: 700;
    font-size: 78px;
  }
  .doctor-name {
    fill: var(--white);
    font-family: "Lexend", sans-serif;
    font-weight: 400;
    font-size: 80px;
  }
  .phone {
    fill: var(--white);
    font-family: "Lexend", sans-serif;
    font-weight: 800;
    font-size: 82px;
  }
  .accent-line {
    stroke: var(--mint);
    stroke-width: 4.5;
    stroke-linecap: round;
  }
</style>
</head>
<body>
  <main class="sign">
    <div class="doctor-photo" role="img" aria-label="Portrait of the clinic's doctor in a dark suit, white shirt and purple tie"></div>

    <svg class="artwork" width="1200" height="900" viewBox="0 0 1200 900" xmlns="http://www.w3.org/2000/svg">
      <polygon class="card-back" points="665,26 1138,206 959,679 486,499" fill="var(--purple-shadow)"/>
      <polygon class="card-front" points="628,45 1120,171 995,661 505,534" fill="var(--purple)"/>

      <line class="accent-line" x1="471" y1="129" x2="735" y2="129"/>
      <line class="accent-line" x1="558" y1="156" x2="674" y2="156"/>
      <line class="accent-line" x1="937" y1="550" x2="1066" y2="550"/>
      <line class="accent-line" x1="838" y1="577" x2="1099" y2="577"/>

      <text class="headline">
        <tspan x="613" y="244">Lose Up To</tspan>
        <tspan x="613" y="334">1 Pound</tspan>
        <tspan x="613" y="423">Of Fat</tspan>
        <tspan x="613" y="511">Per Day</tspan>
      </text>

      <text class="doctor-name" x="507" y="748">DR Halvers’</text>
      <text class="phone" x="504" y="833" textLength="544" lengthAdjust="spacingAndGlyphs">555-206–3948</text>
    </svg>
  </main>
</body>
</html>
```